Letter Head Design - Finance industry

Design a letterhead to match the logo. Needs to be clean, simple and crisp. I'm open to suggestions. Will be using the logo that was submitted last with the W crossed over

Target Market(s)

Small medium businesses and government department's

Industry/Entity Type

Industry

Font styles to use
Sans Serif

Colors
cadf82
bcd85c
acd036
9bcb3c
e9e9e9
aaaaaa
000000
7f7f7f
b7b7b7

Requirements
Must have
• Need to display: Logo, Business address, ABN number, ASIC register number, contact phone, website, company email. Details are as per below:

Suite 4B Level 17
Marlowe Crest Tower
9 Kestin Lane
Sydney NSW 2000
Landline Ph: 02 9417 3065
Ph: 1300 5914 37
Email: enquiries@corvalmoney.com.au
W: www.corvalmoney.com.au

On the footer, the details below need to be specified:
ABN: 48 703 591 236
ASIC Registration Number: 73 418806521

Should not have
• No imagery or design that is not in line with the logo

```html
<!DOCTYPE html>
<html lang="en">
<head>
<meta charset="utf-8">
<title>Corval Money – Letterhead</title>
<link rel="stylesheet" href="https://fonts.googleapis.com/css2?family=EB+Garamond:wght@400;500;600&display=swap">
<style>
  :root {
    --backdrop: #e9e9e9;
    --paper: #ffffff;
    --green: #acd036;
    --green-soft: #bcd85c;
    --ink: #000000;
    --ink-mid: #7f7f7f;
    --ink-light: #aaaaaa;
    --brand-grey: #6f6f6f;
  }
  * { margin: 0; padding: 0; box-sizing: border-box; }
  html, body {
    width: 1200px; height: 900px; overflow: hidden;
    background: var(--backdrop);
    font-family: "EB Garamond", Georgia, serif;
    color: var(--ink);
  }
  .letterhead {
    position: absolute; left: 306px; top: 35px;
    width: 590px; height: 833px;
    background: var(--paper);
    box-shadow: 0 2px 8px rgba(0,0,0,0.18);
    overflow: hidden;
  }
  .brand {
    position: absolute; left: 54px; top: 58px;
    display: flex; align-items: center; gap: 12px;
  }
  .brand-mark {
    width: 48px; height: 48px; border-radius: 50%;
    background: var(--green);
  }
  .brand-name {
    font-size: 29px; line-height: 27px; font-weight: 500;
    color: var(--brand-grey);
  }
  .office {
    position: absolute; left: 398px; top: 35px;
    font-size: 9px; line-height: 10px;
  }
  .office-address { font-weight: 600; color: var(--ink); }
  .office-contact { margin-top: 9px; color: var(--ink-mid); }
  .letter-body {
    position: absolute; left: 194px; top: 220px; width: 366px;
    font-size: 11.2px; line-height: 15px;
  }
  .letter-body p + p { margin-top: 15px; }
  .footer-wave { position: absolute; left: 0; bottom: 0; width: 590px; height: 80px; }
  .footer-details {
    position: absolute; left: 194px; right: 36px; top: 779px;
    display: flex; justify-content: space-between;
    font-size: 9px; color: var(--ink);
  }
</style>
</head>
<body>
  <main class="letterhead">
    <div class="brand">
      <span class="brand-mark"></span>
      <span class="brand-name">Corval<br>Money</span>
    </div>

    <address class="office" style="font-style:normal">
      <div class="office-address">
        Suite 4B Level 17<br>
        Marlowe Crest Tower<br>
        9 Kestin Lane<br>
        Sydney NSW 2000
      </div>
      <div class="office-contact">
        Landline: 02 9417 3065<br>
        Phone: 1300 5914 37<br>
        Email: enquiries@corvalmoney.com.au<br>
        www.corvalmoney.com.au
      </div>
    </address>

    <section class="letter-body">
      <p>Lorem ipsum dolor sit amet, eum in accusam scripserit, ius oblique repudiandae cu. Ea tation indoctum sed, his id inciderint intellegebat, eam et illum suavitate. Vix te discere accumsan disputando, te elit regione cum, id vis veniam prompta docendi. Cibo doming mediocrem an usu, stet solet corpora mel ex. An homero petentium quo.</p>
      <p>Error doming ius ne, pri ut labores scaevola. Est noster offendit cu, ne platonem comprehensam sea, at vel iudico essent. Ea eum equidem docendi sententiae, magna audiam ne quo. Natum rationibus mea ei, eum in clita soleat. Meis omnesque an qui, mea id oblique civibus copiosae, sit et quot aliquam forensibus. Hinc ignota dolorum an eos, hinc recusabo an nam.</p>
      <p>Inimicus scriptorem scribentur cum eu, vel ne vivendo ancillae intellegam, in reque equidem neglegentur mei. Dico nullam patrioque ad per, est ea tritani placerat, at duo atqui deserunt. Eos facer viderer te. Ius illum ceteros volutpat cu, error dolorum eu pro, has te dicit definitionem.</p>
      <p>Dico omittantur mediocritatem ea sed, te atqui congue tantas duo. Debet mucius ei qui, eam in offendit senserit instructior, altera civibus eum te. Ei sit facer laudem discere, prodesset liberavisse in pro, usu sale fierent ne. Labore inermis ullamcorper sea at, putant dissentias necessitatibus mea cu. At mel soluta dolores repudiare, adhuc convenire cu pri.</p>
      <p>Essent sanctus at ius, sea in dicant integre, dolorem tibique ullamcorper ne has. Te verterem euripidis nam. Vis ullum perpetua no, at mel deserunt electram honestatis. Minimum oportere principes mel ne.</p>
    </section>

    <svg class="footer-wave" viewBox="0 0 590 80" preserveAspectRatio="none" aria-hidden="true">
      <path d="M0,2 Q250,70 590,45 L590,80 L0,80 Z" fill="var(--green)"/>
    </svg>

    <footer class="footer-details">
      <span>ABN: 48 703 591 236</span>
      <span>ASIC Registration Number: 73 418806521</span>
    </footer>
  </main>
</body>
</html>
```